A modern, fresh introduction to Buddhism

I need a book cover for an A6 sized book to be used both for ebook and hard copy. The author is a young, modern Buddhist teacher of high standing who has written this short intro to Buddhism in an informal Q & As format using modern, accessible language to convey profound and meaningful ideas to the general public. The author is Tibetan, but teaches worldwide and is very personable and dynamic. The cover should portray this and have a fresh yet authentic feel to it (nothing new-agey!). Please see the author's websites www.norvalemtasheteacher.org and www.pwrt.org for reference, but do not feel that the design must align completely with the website designs.

Target Market(s)

General public both in Europe and America and in Asia ranging from teenagers to the elderly. A really broad audience.

Industry/Entity Type

Teacher

Requirements
Must have
• Please include the following text that on the front cover:

A Window onto Stillness

By Drawa Tsomen Lhundrup

Please include the following on the back cover:

Yunor Trenpa Publications (with attached logo above it)
Nice to have
• A simplistic, artistic, and modern look without any traditional religious images.
Should not have
• No buddha images or religious images. I would prefer a more simplistic, modern and artistic look.

```html
<!DOCTYPE html>
<html lang="en">
<head>
<meta charset="utf-8">
<title>A Window onto Stillness — Cover Spread</title>
<link rel="stylesheet" href="https://fonts.googleapis.com/css2?family=Roboto:wght@300;400;500&display=swap">
<style>
  :root {
    --page: #ffffff;
    --cover-slate: #464349;
    --spine-slate: #48454b;
    --title-orange: #ec8420;
    --author-white: #ffffff;
    --soft-grey: #d8d6da;
    --photo-dark: #1c1b1a;
    --photo-mid: #5a5754;
    --photo-light: #c9c6c0;
  }
  html, body {
    margin: 0;
    padding: 0;
    width: 1200px;
    height: 900px;
    overflow: hidden;
    background: var(--page);
  }
  .spread {
    position: relative;
    width: 1200px;
    height: 900px;
    font-family: "Roboto", Arial, sans-serif;
  }
  .back-cover {
    position: absolute;
    left: 89px;
    top: 109px;
    width: 482px;
    height: 681px;
    background: var(--cover-slate);
  }
  .publisher-mark {
    position: absolute;
    left: 192px;
    top: 455px;
    width: 99px;
    height: 99px;
    border: 1px solid var(--soft-grey);
    border-radius: 50%;
    box-sizing: border-box;
  }
  .publisher-name {
    position: absolute;
    left: 0;
    width: 100%;
    top: 576px;
    text-align: center;
    color: var(--soft-grey);
    font-weight: 300;
    font-size: 16px;
    line-height: 20px;
    letter-spacing: 0.2px;
    margin: 0;
  }
  .spine {
    position: absolute;
    left: 571px;
    top: 109px;
    width: 57px;
    height: 681px;
    background: var(--spine-slate);
  }
  .spine-text {
    position: absolute;
    left: 50%;
    top: 96px;
    transform: translateX(-50%);
    writing-mode: vertical-rl;
    color: var(--soft-grey);
    font-weight: 300;
    font-size: 14.5px;
    letter-spacing: 1.2px;
    white-space: nowrap;
    margin: 0;
  }
  .front-cover {
    position: absolute;
    left: 628px;
    top: 109px;
    width: 483px;
    height: 681px;
    overflow: hidden;
  }
  .cover-photo {
    position: absolute;
    inset: 0;
    background:
      linear-gradient(100deg, transparent 0 48%, rgba(201,198,192,0.0) 48%, rgba(201,198,192,0.55) 62%, rgba(220,217,211,0.7) 80%, rgba(120,117,113,0.3) 100%),
      linear-gradient(90deg, #2a2624 0 3%, #4a3a2e 3% 7%, var(--photo-dark) 7% 9%, #3e3c3a 9% 30%, var(--photo-mid) 45%, #6f6c68 100%),
      var(--photo-dark);
  }
  .cover-title {
    position: absolute;
    left: 103px;
    top: 93px;
    margin: 0;
    color: var(--title-orange);
    font-weight: 500;
    font-size: 37px;
    line-height: 47px;
  }
  .cover-author {
    position: absolute;
    left: 106px;
    top: 210px;
    margin: 0;
    color: var(--author-white);
    font-weight: 500;
    font-size: 20px;
  }
</style>
</head>
<body>
  <main class="spread">
    <section class="back-cover">
      <div class="publisher-mark" aria-hidden="true"></div>
      <p class="publisher-name">Yunor Trenpa Publications</p>
    </section>

    <section class="spine">
      <p class="spine-text">A WINDOW ONTO STILLNESS&nbsp;&nbsp;BY DRAWA TSOMEN LHUNDRUP</p>
    </section>

    <section class="front-cover">
      <div class="cover-photo" role="img" aria-label="Photograph of a shaft of sunlight falling across a rough plastered wall beside a dark wooden door frame, with a small orange butterfly resting in the light"></div>
      <h1 class="cover-title">A Window<br>onto Stillness</h1>
      <p class="cover-author">By Drawa Tsomen Lhundrup</p>
    </section>
  </main>
</body>
</html>
```